Wedding Invitation

We need a two cultural pieces put together in a wedding invitation. The colours are silver blue white. We are looking for light colours. The design should be light and breezy as possible as it is a beach wedding. The date for the wedding is March 21st 2014. Due to a breakdown in another designer we now find ourselves having to rush a design. We need the design in two days if possible of course.

Kind Regards
Hester Lanowa

```html
<!DOCTYPE html>
<html lang="en">
<head>
<meta charset="utf-8">
<title>Wedding Invitation – Marisol &amp; Tariq</title>
<link rel="stylesheet" href="https://fonts.googleapis.com/css2?family=Italianno&family=Pinyon+Script&family=Arimo&display=swap">
<style>
  :root {
    --paper: #ffffff;
    --ink: #4e5b68;
    --ink-shadow: #c9d2db;
    --crop: #6b6b6b;
    --sea-blue: #8fb8d8;
    --sky-blue: #c6dcee;
    --silver: #d3d9df;
    --mist: #f3f6f9;
  }
  * { margin: 0; padding: 0; box-sizing: border-box; }
  html, body {
    width: 1200px; height: 2162px; overflow: hidden;
    background: var(--paper);
  }
  .invitation {
    position: relative; width: 1200px; height: 2162px;
    background: var(--paper);
    font-family: "Italianno", cursive;
    color: var(--ink);
  }
  .crop-marks { position: absolute; inset: 0; }
  .star-band {
    position: absolute;
    border-radius: 4px;
    background: linear-gradient(180deg, var(--sky-blue), var(--sea-blue) 50%, var(--sky-blue));
  }
  .star-band--top { left: 130px; top: 198px; width: 918px; height: 112px; }
  .star-band--bottom { left: 140px; top: 1840px; width: 929px; height: 82px; }
  .koru {
    position: absolute; z-index: 0;
    border-radius: 50%;
    background: radial-gradient(ellipse at center, var(--mist) 0%, rgba(243,246,249,0.5) 55%, rgba(255,255,255,0) 75%);
  }
  .koru--top { left: 560px; top: 330px; width: 560px; height: 260px; }
  .koru--bottom { left: 80px; top: 1570px; width: 620px; height: 250px; }
  .star-medallion {
    position: absolute; left: 473px; top: 875px; width: 256px; height: 222px;
    border-radius: 50%;
    background: radial-gradient(circle, var(--sea-blue) 0%, var(--sea-blue) 40%, var(--sky-blue) 85%, var(--silver) 100%);
  }
  .verse, .couple, .details, .reception { position: absolute; z-index: 1; }
  .verse {
    left: 0; width: 1200px; top: 469px;
    text-align: center; font-size: 72px; line-height: 54px;
    padding-left: 40px;
  }
  .couple {
    font-family: "Pinyon Script", cursive; font-weight: 400;
    font-size: 92px; line-height: 1; white-space: nowrap;
    text-shadow: 4px 4px 0 var(--ink-shadow);
  }
  .couple--first { left: 348px; top: 640px; }
  .couple--second { left: 415px; top: 722px; }
  .details {
    left: 0; width: 1200px; top: 1156px;
    text-align: center; font-size: 68px; line-height: 52px;
    padding-right: 10px;
  }
  .reception {
    left: 0; width: 1200px; top: 1636px;
    text-align: center; font-size: 57px; line-height: 56px;
    padding-right: 10px;
  }
  .trim-size {
    position: absolute; left: 830px; top: 2032px;
    font-family: "Arimo", sans-serif; font-size: 20px; color: #222;
  }
</style>
</head>
<body>
<main class="invitation">
  <svg class="crop-marks" width="1200" height="2162" viewBox="0 0 1200 2162" aria-hidden="true">
    <g stroke="var(--crop)" stroke-width="1.5">
      <line x1="171" y1="0" x2="171" y2="112"/>
      <line x1="1030" y1="0" x2="1030" y2="112"/>
      <line x1="0" y1="171" x2="112" y2="171"/>
      <line x1="1087" y1="171" x2="1200" y2="171"/>
      <line x1="0" y1="1991" x2="112" y2="1991"/>
      <line x1="1087" y1="1991" x2="1200" y2="1991"/>
      <line x1="171" y1="2045" x2="171" y2="2162"/>
      <line x1="1030" y1="2045" x2="1030" y2="2162"/>
    </g>
  </svg>

  <div class="star-band star-band--top" role="img" aria-label="Band of interlocking six-pointed star motifs"></div>
  <div class="koru koru--top" role="img" aria-label="Faint silver koru fern-frond scroll ornament"></div>

  <p class="verse">Two hearts from world's apart<br>Now celebrate a new start</p>

  <h1 class="couple couple--first">Marisol &amp;</h1>
  <h1 class="couple couple--second">Tariq</h1>

  <div class="star-medallion" role="img" aria-label="Medallion of clustered six-pointed stars"></div>

  <p class="details">
    invite you to the celebration<br>
    of their wedding<br>
    on Friday the twenty first of March<br>
    two thousand and fourteen<br>
    at four o'clock<br>
    The ceremony will be held<br>
    at Harbour Point Lookout, Seabreeze<br>
    Shoreline Parade<br>
    Seabreeze
  </p>
  <p class="reception">Reception to follow</p>

  <div class="koru koru--bottom" role="img" aria-label="Faint silver koru fern-frond scroll ornament"></div>
  <div class="star-band star-band--bottom" role="img" aria-label="Band of interlocking six-pointed star motifs"></div>

  <p class="trim-size">99mm X 210mm</p>
</main>
</body>
</html>
```